Orlent Telecom Business Card Competition

High quality international communications for consumers and business. We are re-designing our website and re-branding. Our current (old) website can be viewed at www.goorlent-example.net Vision statement - We enable people and communities to build and maintain strong and lasting global connections This is the brand image that we are trying to get across: •Quality—Orlent delivers the highest quality connections wherever you need to communicate. •Service—Orlent is always there for you, with the industry-leading service that promises to ensure that every experience is a good one. •Value—Orlent provides the best value in the global communications market. Typical messaging: Connecting the Most Important People in the World. Focus on international communications

We want to convey our service quality and that we really care about the service we provide and our customers. We want to emphasis the international aspect of our business. We want to make it personal, but it has to relate to business as well as individuals. We want the card to be unique in design but clear enough to read. We want a business prospect as well as a regular person to look at our card and know what we do.

Target Market(s)

Consumer - multi-ethnic consumer base living in the US calling, texting and connecting with family and friends in countries around the world 2. Busine

Industry/Entity Type

Communications

Requirements
Must have
• 1. Logo must be visible (see uploaded)

2.Artist can use variations of our company colors to accent our logo:

Hex Codes:
Magenta = ab3179
Blue = 2895c0
Green = 8ebb3f

3.Must have the following slogan visible: Because Every Call Matters

below are the required data fields:

Full Name: Mark Tallow
Position: Chief Financial Officer
Office: +1 608-441-2871 ext.318
Mobile: +1 608-441-2871
Fax: +1 608-441-2871
Email: MarkT@goorlent-example.net
URL: www.goorlent-example.net
Address:
71820 Brindle Avenue
suite 412
Larkfield, OR 97118
USA

Nice to have
• Die cut cards or uniquely shaped cards would be interesting to see but not required

```html
<!DOCTYPE html>
<html lang="en">
<head>
<meta charset="utf-8">
<title>Orlent Telecom Business Card</title>
<link rel="stylesheet" href="https://fonts.googleapis.com/css2?family=Open+Sans:wght@400;600;700&display=swap">
<style>
  :root {
    --blue: #2895c0;
    --blue-sky: #7fdcfb;
    --blue-mid: #3fb6ea;
    --magenta: #ab3179;
    --magenta-light: #e0589f;
    --magenta-mid: #d24a93;
    --green: #8ebb3f;
    --green-bright: #84c622;
    --green-light: #a3dc55;
    --white: #ffffff;
    --stage-dark: #1f1f1f;
    --stage-light: #4a4a4a;
  }
  * { box-sizing: border-box; margin: 0; padding: 0; }
  html, body { width: 1200px; height: 675px; overflow: hidden; }
  body {
    font-family: "Open Sans", sans-serif;
    background: radial-gradient(ellipse at 45% 40%, var(--stage-light), var(--stage-dark) 75%);
    position: relative;
  }
  .card {
    position: absolute;
    overflow: hidden;
    box-shadow: 0 10px 28px rgba(0,0,0,0.55);
  }

  /* Front */
  .card-front { left: 55px; top: 45px; width: 545px; height: 282px; display: flex; }
  .band { height: 100%; }
  .band-blue { width: 40%; background: radial-gradient(circle at 60% 60%, var(--blue-sky), var(--blue-mid) 72%); }
  .band-magenta { width: 16%; background: linear-gradient(180deg, var(--magenta-mid), var(--magenta-light)); }
  .band-green { width: 44%; background: linear-gradient(180deg, var(--green-bright), var(--green-light)); }
  .front-content {
    position: absolute; left: 0; top: 0; width: 100%; height: 100%;
  }
  .front-brand {
    position: absolute; left: 0; width: 100%; top: 96px;
    display: flex; justify-content: center; align-items: center; gap: 12px;
    color: var(--white); font-weight: 700; font-size: 34px; letter-spacing: 1px;
    padding-right: 50px;
  }
  .brand-mark { width: 14px; height: 14px; background: var(--white); border-radius: 50%; }
  .slogan {
    position: absolute; left: 0; width: 100%; top: 216px;
    text-align: center; padding-right: 50px;
    color: var(--white); font-size: 17px;
    text-decoration: underline; text-underline-offset: 3px;
  }

  /* Back */
  .card-back {
    left: 500px; top: 330px; width: 610px; height: 320px;
    background: linear-gradient(180deg, var(--green-bright), var(--green-light));
  }
  .back-header {
    height: 104px;
    background: linear-gradient(180deg, #48b8f0, var(--blue-sky));
    border-bottom: 7px solid var(--magenta-light);
    position: relative;
  }
  .logo-box {
    position: absolute; left: 31px; top: 14px;
    width: 175px; height: 72px;
    background: var(--white);
    display: flex; align-items: center; justify-content: center;
  }
  .logo-box .brand-name { color: var(--blue); font-weight: 700; font-size: 32px; }
  .divider {
    position: absolute; left: 285px; top: 114px;
    width: 2px; height: 176px; background: var(--magenta);
  }
  .person {
    position: absolute; left: 0; width: 285px; top: 168px;
    text-align: center; color: var(--white);
  }
  .person-name { font-size: 23px; font-weight: 700; line-height: 1.2; }
  .person-title { font-size: 11px; font-weight: 600; margin-top: 3px; }
  .contacts {
    position: absolute; left: 328px; top: 144px;
    color: var(--white); font-size: 12px; font-weight: 600; line-height: 1.3;
    list-style: none;
  }
  .contacts li { display: flex; align-items: flex-start; gap: 7px; margin-bottom: 4px; }
  .contacts li.office { margin-bottom: 5px; }
  .contacts .with-icon { padding-left: 26px; }
  .contacts .icon { width: 14px; height: 14px; flex: none; margin-top: 1px; }
  .website {
    position: absolute; left: 22px; bottom: 20px;
    display: flex; align-items: center; gap: 9px;
    color: var(--white); font-size: 13px; font-weight: 700;
    border-bottom: 1.5px solid var(--white); padding-bottom: 1px;
  }
</style>
</head>
<body>

<section class="card card-front" aria-label="Business card front">
  <div class="band band-blue"></div>
  <div class="band band-magenta"></div>
  <div class="band band-green"></div>
  <div class="front-content">
    <div class="front-brand"><span class="brand-mark"></span>Orlent Telecom</div>
    <p class="slogan">Because Every Call Matters</p>
  </div>
</section>

<section class="card card-back" aria-label="Business card back">
  <header class="back-header">
    <div class="logo-box"><span class="brand-name">Orlent</span></div>
  </header>
  <div class="person">
    <p class="person-name">Mark Tallow</p>
    <p class="person-title">Chief Financial Officer</p>
  </div>
  <div class="divider"></div>
  <ul class="contacts">
    <li class="office">Office: +1 608-441-2871 ext.318</li>
    <li class="with-icon">
      <svg class="icon" viewBox="0 0 14 14" aria-label="Mobile"><rect x="4" y="1" width="6" height="12" rx="1" fill="none" stroke="#fff" stroke-width="1.3"/><line x1="6" y1="11" x2="8" y2="11" stroke="#fff"/></svg>
      <span>+1 608-441-2871</span>
    </li>
    <li class="with-icon">
      <svg class="icon" viewBox="0 0 14 14" aria-label="Fax"><rect x="3" y="1" width="8" height="5" fill="none" stroke="#fff" stroke-width="1.2"/><rect x="1" y="6" width="12" height="7" fill="none" stroke="#fff" stroke-width="1.2"/><line x1="4" y1="9" x2="10" y2="9" stroke="#fff"/></svg>
      <span>+1 608-441-2871</span>
    </li>
    <li class="with-icon">
      <svg class="icon" viewBox="0 0 14 14" aria-label="Email"><rect x="1" y="3" width="12" height="8" fill="none" stroke="#fff" stroke-width="1.2"/><polyline points="1,3 7,8 13,3" fill="none" stroke="#fff" stroke-width="1.2"/></svg>
      <span>MarkT@goorlent-example.net</span>
    </li>
    <li class="with-icon">
      <svg class="icon" viewBox="0 0 14 14" aria-label="Address"><polyline points="1,7 7,2 13,7" fill="none" stroke="#fff" stroke-width="1.3"/><rect x="3" y="7" width="8" height="6" fill="none" stroke="#fff" stroke-width="1.2"/></svg>
      <span>71820 Brindle Avenue<br>suite 412<br>Larkfield, OR 97118<br>USA</span>
    </li>
  </ul>
  <div class="website">
    <svg width="16" height="14" viewBox="0 0 16 14" aria-label="Website"><rect x="1" y="1" width="14" height="9" fill="none" stroke="#fff" stroke-width="1.3"/><line x1="5" y1="13" x2="11" y2="13" stroke="#fff" stroke-width="1.3"/><line x1="8" y1="10" x2="8" y2="13" stroke="#fff"/></svg>
    <span>www.goorlent-example.net</span>
  </div>
</section>

</body>
</html>
```